Flyer for a Payroll and Bookkeeping Companmy

Need a brochure to highlight our costs and service to hand out to clients.

Please see attachments for more information.

Industry/Entity Type

It Service

```html
<!DOCTYPE html>
<html lang="en">
<head>
<meta charset="utf-8">
<title>Harbor Ridge – Bookkeeping &amp; Payroll Pricing</title>
<link rel="stylesheet" href="https://fonts.googleapis.com/css2?family=PT+Sans:wght@400;700&family=Open+Sans:wght@400;600;700&display=swap">
<style>
:root{
  --orange:#e8862a;
  --orange-soft:#f6c79a;
  --blue:#1572c4;
  --blue-row:#cfdcf1;
  --ink:#222;
  --stage:#555;
  --white:#fff;
}
*{box-sizing:border-box;margin:0;padding:0}
html,body{width:1200px;height:858px;overflow:hidden;background:var(--stage)}
body{position:relative;font-family:"Open Sans",sans-serif;color:var(--ink)}
.page{position:absolute;top:17px;width:570px;height:737px;background:var(--white);overflow:hidden}
.page--front{left:21px}
.page--back{left:611px}
.photo{position:absolute;left:0;top:0;width:100%}
.photo--front{height:293px;background:linear-gradient(120deg,#e6b77a 0%,#c7cbd0 40%,#6f87a8 75%,#3f5a82 100%)}
.photo--back{height:374px;background:linear-gradient(110deg,#dfe7ee 0%,#f4f6f8 45%,#c8cfd2 75%,#9ea7a8 100%)}
.brand{position:absolute;display:flex;align-items:center;gap:8px}
.brand__mark{width:34px;height:34px;border-radius:50%;background:var(--orange);flex:none}
.brand__name{font-family:"PT Sans",sans-serif;font-weight:700;font-size:23px;color:var(--blue);white-space:nowrap}
.page--front .brand{left:34px;top:340px}
.page--back .brand{left:34px;top:428px}
.title{position:absolute;font-family:"PT Sans",sans-serif;font-weight:700;line-height:.9;letter-spacing:.3px;white-space:nowrap}
.title--front{left:215px;top:306px;font-size:53px;color:var(--orange)}
.title--back{left:215px;top:391px;font-size:51px;color:var(--blue)}
.title span{display:block}

.pricing{position:absolute;left:34px;top:418px;width:502px;border-collapse:collapse;table-layout:fixed;font-size:10.4px}
.pricing td,.pricing th{border:1px solid var(--blue);text-align:center;vertical-align:middle;line-height:1.1}
.pricing col.svc{width:146px}
.pricing .services{background:var(--blue);color:var(--white);font-weight:700;font-size:15px;font-family:"PT Sans",sans-serif}
.pricing .tier{background:var(--orange-soft);font-weight:400;font-size:10px;height:17px}
.pricing .price{background:var(--orange);color:var(--white);font-family:"PT Sans",sans-serif;font-weight:700;font-size:21px;height:25px}
.pricing .price sup{font-size:11px;vertical-align:9px}
.pricing tbody tr:nth-child(even){background:var(--blue-row)}
.pricing .label{font-weight:700;font-size:10px}
.pricing .label small{display:block;font-weight:400;font-size:7.5px}
.pricing .freq{color:var(--orange);font-weight:600;font-size:10px}
.tick{display:inline-block;width:15px;height:13px;vertical-align:-2px}
.cross{display:inline-block;width:12px;height:12px}
.fee{display:block;color:var(--orange);font-weight:700;font-size:9.5px}

.footer{position:absolute;left:0;bottom:0;width:100%;height:66px;display:flex;align-items:center;justify-content:center;gap:14px;color:var(--white);font-family:"PT Sans",sans-serif;font-size:13.5px}
.footer--front{background:var(--orange)}
.footer--back{background:var(--blue)}
.footer__item{display:flex;align-items:center;gap:4px;white-space:nowrap}
.footer__item svg{width:13px;height:14px;fill:var(--white)}

.offer{position:absolute;left:34px;top:524px;display:flex;align-items:center;font-family:"PT Sans",sans-serif;font-weight:700;font-size:17.5px;line-height:1.15}
.offer__item{display:flex;align-items:center;gap:8px}
.offer__icon{width:66px;height:66px;flex:none}
.offer__plus{color:var(--blue);font-size:24px;margin:0 6px}
.offer__item--fees{margin-left:40px;color:var(--orange)}
.note{position:absolute;left:34px;top:621px;font-size:11.2px;line-height:1.4;white-space:nowrap}
.note em{font-style:normal;color:var(--orange)}
</style>
</head>
<body>

<section class="page page--front">
  <div class="photo photo--front" role="img" aria-label="Photo of a person working a calculator at a desk with paperwork"></div>
  <div class="brand"><span class="brand__mark"></span><span class="brand__name">Harbor Ridge</span></div>
  <h1 class="title title--front"><span>Bookkeeping</span><span>Pricing</span></h1>

  <table class="pricing">
    <colgroup><col class="svc"><col><col><col><col></colgroup>
    <thead>
      <tr><th class="services" rowspan="2">SERVICES</th><th class="tier">Premium</th><th class="tier">Entrepreneur</th><th class="tier">Growth</th><th class="tier">Start Up</th></tr>
      <tr><th class="price"><sup>$</sup>999</th><th class="price"><sup>$</sup>599</th><th class="price"><sup>$</sup>299</th><th class="price"><sup>$</sup>149</th></tr>
    </thead>
    <tbody>
      <tr style="height:19px"><td class="label">Employees</td><td>Around <b>10+</b></td><td>Around <b>5-9</b></td><td>Around <b>2-5</b></td><td>Around <b>1-2</b></td></tr>
      <tr style="height:19px"><td class="label">Transactions / Month</td><td>Up to <b>250</b></td><td>Up to <b>150</b></td><td>Up to <b>75</b></td><td>Up to <b>50</b></td></tr>
      <tr style="height:23px"><td class="label">Bookkeeping</td>
        <td class="freq"><svg class="tick" viewBox="0 0 15 13"><path d="M1 7l4 4 9-10" fill="none" stroke="#e8862a" stroke-width="2.2"/></svg> Weekly</td>
        <td class="freq"><svg class="tick" viewBox="0 0 15 13"><path d="M1 7l4 4 9-10" fill="none" stroke="#e8862a" stroke-width="2.2"/></svg> Weekly</td>
        <td class="freq"><svg class="tick" viewBox="0 0 15 13"><path d="M1 7l4 4 9-10" fill="none" stroke="#e8862a" stroke-width="2.2"/></svg> Monthly</td>
        <td class="freq"><svg class="tick" viewBox="0 0 15 13"><path d="M1 7l4 4 9-10" fill="none" stroke="#e8862a" stroke-width="2.2"/></svg> Quarterly</td></tr>
      <tr style="height:23px"><td class="label">Financial Reports &amp; Review</td>
        <td class="freq"><svg class="tick" viewBox="0 0 15 13"><path d="M1 7l4 4 9-10" fill="none" stroke="#e8862a" stroke-width="2.2"/></svg> Monthly</td>
        <td class="freq"><svg class="tick" viewBox="0 0 15 13"><path d="M1 7l4 4 9-10" fill="none" stroke="#e8862a" stroke-width="2.2"/></svg> Monthly</td>
        <td class="freq"><svg class="tick" viewBox="0 0 15 13"><path d="M1 7l4 4 9-10" fill="none" stroke="#e8862a" stroke-width="2.2"/></svg> Monthly</td>
        <td class="freq"><svg class="tick" viewBox="0 0 15 13"><path d="M1 7l4 4 9-10" fill="none" stroke="#e8862a" stroke-width="2.2"/></svg> Quarterly</td></tr>
      <tr style="height:27px"><td class="label">Support<small>(Phone and Chat)</small></td>
        <td><svg class="tick" viewBox="0 0 15 13"><path d="M1 7l4 4 9-10" fill="none" stroke="#e8862a" stroke-width="2"/></svg></td>
        <td><svg class="tick" viewBox="0 0 15 13"><path d="M1 7l4 4 9-10" fill="none" stroke="#e8862a" stroke-width="2"/></svg></td>
        <td><svg class="tick" viewBox="0 0 15 13"><path d="M1 7l4 4 9-10" fill="none" stroke="#e8862a" stroke-width="2"/></svg></td>
        <td><svg class="tick" viewBox="0 0 15 13"><path d="M1 7l4 4 9-10" fill="none" stroke="#e8862a" stroke-width="2"/></svg></td></tr>
      <tr style="height:27px"><td class="label">Online Collaboration Portal<small>(Shared Drive)</small></td>
        <td><svg class="tick" viewBox="0 0 15 13"><path d="M1 7l4 4 9-10" fill="none" stroke="#e8862a" stroke-width="2"/></svg></td>
        <td><svg class="tick" viewBox="0 0 15 13"><path d="M1 7l4 4 9-10" fill="none" stroke="#e8862a" stroke-width="2"/></svg></td>
        <td><svg class="tick" viewBox="0 0 15 13"><path d="M1 7l4 4 9-10" fill="none" stroke="#e8862a" stroke-width="2"/></svg></td>
        <td><svg class="tick" viewBox="0 0 15 13"><path d="M1 7l4 4 9-10" fill="none" stroke="#e8862a" stroke-width="2"/></svg></td></tr>
      <tr style="height:24px"><td class="label">Business Tax Return</td>
        <td><svg class="tick" viewBox="0 0 15 13"><path d="M1 7l4 4 9-10" fill="none" stroke="#e8862a" stroke-width="2"/></svg></td>
        <td><svg class="tick" viewBox="0 0 15 13"><path d="M1 7l4 4 9-10" fill="none" stroke="#e8862a" stroke-width="2"/></svg></td>
        <td>$799</td><td>$599</td></tr>
      <tr style="height:36px"><td class="label">Bill Pay<small>(with Approval Process)</small></td>
        <td><svg class="tick" viewBox="0 0 15 13"><path d="M1 7l4 4 9-10" fill="none" stroke="#e8862a" stroke-width="2"/></svg><span class="fee">$5 / Payment</span></td>
        <td><svg class="cross" viewBox="0 0 12 12"><path d="M1 1l10 10M11 1L1 11" stroke="#222" stroke-width="1.4"/></svg></td>
        <td><svg class="cross" viewBox="0 0 12 12"><path d="M1 1l10 10M11 1L1 11" stroke="#222" stroke-width="1.4"/></svg></td>
        <td><svg class="cross" viewBox="0 0 12 12"><path d="M1 1l10 10M11 1L1 11" stroke="#222" stroke-width="1.4"/></svg></td></tr>
    </tbody>
  </table>

  <footer class="footer footer--front">
    <span class="footer__item"><svg viewBox="0 0 12 16"><path d="M6 0a6 6 0 0 0-6 6c0 4.5 6 10 6 10s6-5.5 6-10a6 6 0 0 0-6-6zm0 8.5A2.5 2.5 0 1 1 6 3.5a2.5 2.5 0 0 1 0 5z"/></svg>1280 N Elm Ave, Cedar Falls, UT 84020</span>
    <span class="footer__item"><svg viewBox="0 0 16 16"><path d="M3.5 1l3 3-2 2c1 2 3.5 4.5 5.5 5.5l2-2 3 3-2.5 2.5C7 14.5 1.5 9 1 3.5z"/></svg>555-014-2738</span>
    <span class="footer__item"><svg viewBox="0 0 16 16"><path d="M8 0a8 8 0 1 0 0 16A8 8 0 0 0 8 0zm0 1.3c.9 0 2 1.7 2.4 4.7H5.6C6 3 7.1 1.3 8 1.3zM1.4 7.2h3a15 15 0 0 0 0 1.6h-3a6.7 6.7 0 0 1 0-1.6zm4.2 2.8h4.8c-.4 3-1.5 4.7-2.4 4.7S6 13 5.6 10zm6-1.2a15 15 0 0 0 0-1.6h3a6.7 6.7 0 0 1 0 1.6z"/></svg>HarborRidge.com</span>
  </footer>
</section>

<section class="page page--back">
  <div class="photo photo--back" role="img" aria-label="Photo of a person using a tablet at a bright office desk with a computer"></div>
  <div class="brand"><span class="brand__mark"></span><span class="brand__name">Harbor Ridge</span></div>
  <h1 class="title title--back"><span>Simplified</span><span>Payroll Pricing</span></h1>

  <div class="offer">
    <div class="offer__item">
      <svg class="offer__icon" viewBox="0 0 66 66"><circle cx="33" cy="33" r="33" fill="#1572c4"/><circle cx="36" cy="24" r="10" fill="#fff"/><text x="36" y="28.5" font-size="12" font-weight="700" text-anchor="middle" fill="#1572c4" font-family="Open Sans,sans-serif">$</text><path d="M10 42c6-4 12-4 18-1h10c3 0 3 4 0 4h-9 12l10-6c3-1 5 2 2 4l-12 8H10z" fill="#fff"/></svg>
      <span>$25 per<br>Payroll</span>
    </div>
    <span class="offer__plus">+</span>
    <div class="offer__item">
      <svg class="offer__icon" viewBox="0 0 66 66"><circle cx="33" cy="33" r="33" fill="#1572c4"/><circle cx="33" cy="21" r="9" fill="#fff"/><path d="M15 52c0-12 8-19 18-19s18 7 18 19z" fill="#fff"/><circle cx="33" cy="48" r="7" fill="#1572c4" stroke="#fff" stroke-width="1.5"/><text x="33" y="52" font-size="10" font-weight="700" text-anchor="middle" fill="#fff" font-family="Open Sans,sans-serif">$</text></svg>
      <span>$5 per<br>Employee</span>
    </div>
    <div class="offer__item offer__item--fees">
      <svg class="offer__icon" viewBox="0 0 66 66"><circle cx="33" cy="33" r="33" fill="#e8862a"/><circle cx="33" cy="33" r="16" fill="none" stroke="#fff" stroke-width="5" stroke-dasharray="6 4.5"/><circle cx="33" cy="33" r="7" fill="none" stroke="#fff" stroke-width="3"/><path d="M22 46l18-18" stroke="#fff" stroke-width="4" stroke-linecap="round"/></svg>
      <span>No Set Up<br>Fees!</span>
    </div>
  </div>

  <p class="note">Direct deposit only, add $20 per payroll if you elect to have paper checks shipped to you.<br>Minimum charge of two payrolls per month. <em>Cost per employee drops to $4 after 20 employees.</em></p>

  <footer class="footer footer--back">
    <span class="footer__item"><svg viewBox="0 0 12 16"><path d="M6 0a6 6 0 0 0-6 6c0 4.5 6 10 6 10s6-5.5 6-10a6 6 0 0 0-6-6zm0 8.5A2.5 2.5 0 1 1 6 3.5a2.5 2.5 0 0 1 0 5z"/></svg>1280 N Elm Ave, Cedar Falls, UT 84020</span>
    <span class="footer__item"><svg viewBox="0 0 16 16"><path d="M3.5 1l3 3-2 2c1 2 3.5 4.5 5.5 5.5l2-2 3 3-2.5 2.5C7 14.5 1.5 9 1 3.5z"/></svg>555-014-2738</span>
    <span class="footer__item"><svg viewBox="0 0 16 16"><path d="M8 0a8 8 0 1 0 0 16A8 8 0 0 0 8 0zm0 1.3c.9 0 2 1.7 2.4 4.7H5.6C6 3 7.1 1.3 8 1.3zM1.4 7.2h3a15 15 0 0 0 0 1.6h-3a6.7 6.7 0 0 1 0-1.6zm4.2 2.8h4.8c-.4 3-1.5 4.7-2.4 4.7S6 13 5.6 10zm6-1.2a15 15 0 0 0 0-1.6h3a6.7 6.7 0 0 1 0 1.6z"/></svg>HarborRidge.com</span>
  </footer>
</section>

</body>
</html>
```